Business Card - I already have a Logo

I have a logo, I just want a business card designed that uses it. I would like to see designs that are very clean, have a sense of health and wellbeing, up-market clientele.

Target Market(s)

People interested in health and well-being, people with money! Ages 25-70

Industry/Entity Type

Massage Therapy

Contact Information for Business Card

Tove Brinck
Integrative Bodyworker

KaHuna, Remedial, Pregnancy & Maya Abdominal Massage, Body Based Psychology. Health fund rebates available
0437615290
info@wrenmossvale.com.au

Colors
86cfc6
33b8a4
00a990
85cae6
cee9f5
33a6d7
85acd3
3276b5
0355a3

Requirements
Must have
• Clean, simple, elegant design, using my existing logo

```html
<!DOCTYPE html>
<html lang="en">
<head>
<meta charset="utf-8">
<title>Wren Mossvale business cards</title>
<link rel="stylesheet" href="https://fonts.googleapis.com/css2?family=Saira:ital,wght@0,400;0,500;0,600;1,400&display=swap">
<style>
  :root {
    --backdrop: #ecebe8;
    --card-white: #ffffff;
    --sand-deep: #c98a3a;
    --sand-mid: #dcc3a0;
    --sand-light: #efe7dc;
    --stone: #8a7a68;
    --teal: #6cc6cc;
    --navy: #1a54a0;
    --sky: #0aa3dd;
    --sky-deep: #1a5fa8;
    --wordmark: #ffffff;
  }
  * { box-sizing: border-box; margin: 0; padding: 0; }
  html, body { width: 1200px; height: 1200px; overflow: hidden; }
  body {
    background: var(--backdrop);
    font-family: "Saira", sans-serif;
    position: relative;
  }
  .card {
    position: absolute;
    width: 528px;
    height: 316px;
    overflow: hidden;
    box-shadow: 0 2px 6px rgba(0,0,0,0.15);
  }
  .card--front { left: 54px; }
  .card--back { left: 618px; background: var(--card-white); }
  .row-1 { top: 86px; }
  .row-2 { top: 442px; }
  .row-3 { top: 792px; }

  .sandstone {
    position: absolute; inset: 0;
    background:
      radial-gradient(ellipse 45% 70% at 8% 55%, var(--sand-deep) 0%, rgba(201,138,58,0) 75%),
      radial-gradient(ellipse 30% 40% at 95% 85%, var(--stone) 0%, rgba(138,122,104,0) 80%),
      linear-gradient(120deg, var(--sand-mid) 0%, var(--sand-light) 45%, #e6dccd 75%, var(--sand-mid) 100%);
  }
  .brand {
    position: absolute; left: 0; right: 0; top: 80px;
    display: flex; flex-direction: column; align-items: center; gap: 10px;
  }
  .brand-dot {
    width: 90px; height: 90px; border-radius: 50%;
    background: var(--wordmark);
  }
  .brand-name {
    color: var(--wordmark);
    font-weight: 500; font-size: 30px; line-height: 1;
    letter-spacing: -0.5px;
  }

  .disc {
    position: absolute; left: -36px; top: 48px;
    width: 300px; height: 300px;
  }
  .services, .contact {
    position: absolute; right: 22px;
    text-align: right;
    font-size: 14.5px; line-height: 22.5px; font-weight: 500;
    letter-spacing: 0.3px;
  }
  .services { top: 19px; }
  .services li { list-style: none; white-space: nowrap; }
  .bullet {
    display: inline-block; width: 10px; height: 10px; border-radius: 50%;
    margin: 0 6px 0 10px; vertical-align: 0;
  }
  .contact { top: 186px; }
  .person-name { font-size: 18.5px; font-weight: 600; line-height: 24px; }
  .person-role { font-size: 13px; font-style: italic; font-weight: 400; line-height: 16px; margin-bottom: 8px; }
  .contact-line { display: flex; justify-content: flex-end; align-items: center; gap: 8px; }
  .contact-line svg { width: 17px; height: 17px; flex: none; }

  .tone-teal { color: var(--teal); }
  .tone-teal .bullet { background: var(--teal); }
  .tone-navy { color: var(--navy); }
  .tone-navy .bullet { background: var(--navy); }
  .tone-mixed { color: var(--navy); }
  .tone-mixed .bullet { background: var(--navy); }
  .tone-mixed .accent { color: var(--sky); }
</style>
</head>
<body>

<svg width="0" height="0" style="position:absolute" aria-hidden="true">
  <defs>
    <linearGradient id="sky-fill" x1="0" y1="0" x2="1" y2="1">
      <stop offset="0" stop-color="#00b3ea"/>
      <stop offset="1" stop-color="#1a5fa8"/>
    </linearGradient>
    <symbol id="icon-phone" viewBox="0 0 20 20">
      <circle cx="10" cy="10" r="9.5" fill="currentColor"/>
      <path d="M7 5.5c-1 .8-1.3 2.3-.5 4.2.9 2.2 2.5 4 4.4 4.8 1.2.5 2.2.3 2.9-.3l-1.6-1.7-1.3.6c-1-.5-1.9-1.6-2.3-2.6l.9-1.1L7 5.5z" fill="#fff"/>
    </symbol>
    <symbol id="icon-mail" viewBox="0 0 20 20">
      <circle cx="10" cy="10" r="8.8" fill="none" stroke="currentColor" stroke-width="1.4"/>
      <rect x="5.5" y="6.8" width="9" height="6.4" rx="1" fill="none" stroke="currentColor" stroke-width="1.3"/>
      <path d="M5.8 7.2 10 10.6l4.2-3.4" fill="none" stroke="currentColor" stroke-width="1.3"/>
    </symbol>
    <symbol id="icon-web" viewBox="0 0 20 20">
      <circle cx="10" cy="10" r="8.8" fill="none" stroke="currentColor" stroke-width="1.4"/>
      <circle cx="10" cy="10" r="5.4" fill="none" stroke="currentColor" stroke-width="1.1"/>
      <ellipse cx="10" cy="10" rx="2.2" ry="5.4" fill="none" stroke="currentColor" stroke-width="1.1"/>
      <path d="M4.6 10h10.8M5.4 7.4h9.2M5.4 12.6h9.2" stroke="currentColor" stroke-width="1"/>
    </symbol>
  </defs>
</svg>

<!-- Row 1 -->
<section class="card card--front row-1">
  <div class="sandstone" role="img" aria-label="Close-up photograph of weathered ochre and cream sandstone"></div>
  <div class="brand"><span class="brand-dot"></span><span class="brand-name">Wren Mossvale</span></div>
</section>
<section class="card card--back row-1 tone-teal">
  <svg class="disc" viewBox="0 0 300 300" aria-hidden="true"><circle cx="150" cy="150" r="150" fill="var(--teal)"/></svg>
  <ul class="services">
    <li><span class="bullet"></span>KaHuna<span class="bullet"></span>Remedial</li>
    <li><span class="bullet"></span>Pregnancy &amp; Maya Abdominal Massage</li>
    <li><span class="bullet"></span>Body Based Psychology</li>
    <li><span class="bullet"></span>Health fund rebates available</li>
  </ul>
  <div class="contact">
    <p class="person-name">Tove Brinck</p>
    <p class="person-role">Integrative Bodyworker</p>
    <p class="contact-line">0437 615 290 <svg><use href="#icon-phone"/></svg></p>
    <p class="contact-line">info@wrenmossvale.com.au <svg><use href="#icon-mail"/></svg></p>
    <p class="contact-line">www.wrenmossvale.com.au <svg><use href="#icon-web"/></svg></p>
  </div>
</section>

<!-- Row 2 -->
<section class="card card--front row-2">
  <div class="sandstone" role="img" aria-label="Close-up photograph of weathered ochre and cream sandstone"></div>
  <div class="brand"><span class="brand-dot"></span><span class="brand-name">Wren Mossvale</span></div>
</section>
<section class="card card--back row-2 tone-navy">
  <svg class="disc" viewBox="0 0 300 300" aria-hidden="true"><circle cx="150" cy="150" r="150" fill="var(--navy)"/></svg>
  <ul class="services">
    <li><span class="bullet"></span>KaHuna<span class="bullet"></span>Remedial</li>
    <li><span class="bullet"></span>Pregnancy &amp; Maya Abdominal Massage</li>
    <li><span class="bullet"></span>Body Based Psychology</li>
    <li><span class="bullet"></span>Health fund rebates available</li>
  </ul>
  <div class="contact">
    <p class="person-name">Tove Brinck</p>
    <p class="person-role">Integrative Bodyworker</p>
    <p class="contact-line">0437 615 290 <svg><use href="#icon-phone"/></svg></p>
    <p class="contact-line">info@wrenmossvale.com.au <svg><use href="#icon-mail"/></svg></p>
    <p class="contact-line">www.wrenmossvale.com.au <svg><use href="#icon-web"/></svg></p>
  </div>
</section>

<!-- Row 3 -->
<section class="card card--front row-3">
  <div class="sandstone" role="img" aria-label="Close-up photograph of weathered ochre and cream sandstone"></div>
  <div class="brand"><span class="brand-dot"></span><span class="brand-name">Wren Mossvale</span></div>
</section>
<section class="card card--back row-3 tone-mixed">
  <svg class="disc" viewBox="0 0 300 300" aria-hidden="true"><circle cx="150" cy="150" r="150" fill="url(#sky-fill)"/></svg>
  <ul class="services">
    <li><span class="bullet"></span>KaHuna<span class="bullet"></span>Remedial</li>
    <li><span class="bullet"></span><span class="accent">Pregnancy</span> &amp; Maya Abdominal Massage</li>
    <li><span class="bullet"></span>Body Based Psychology</li>
    <li><span class="bullet"></span><span class="accent">Health fund rebates available</span></li>
  </ul>
  <div class="contact">
    <p class="person-name">Tove Brinck</p>
    <p class="person-role accent">Integrative Bodyworker</p>
    <p class="contact-line">0437 615 290 <svg><use href="#icon-phone"/></svg></p>
    <p class="contact-line accent">info@wrenmossvale.com.au <svg><use href="#icon-mail"/></svg></p>
    <p class="contact-line accent">www.wrenmossvale.com.au <svg><use href="#icon-web"/></svg></p>
  </div>
</section>

</body>
</html>
```